Imported Fine Wine E-commerce site

We need an e-commerce site built from scratch. We currently have a website however it is on Magento and would like a more user friendly platform. Not sure if its possible to use any of the information. We're looking for a mostly white clean design with some red to match the logo.

Target Market(s)

30+

Coding

Coded - Design and coding required

Number of Pages Required

5+ page

Colors
ec1f27

Requirements
Must have
• Categories 'Red/White/Bubbles/Mixed cases/Gifts/Wholesale'
'sort by' functions.
Contact us form
Filter by on left hand side, Variety, Price, Region
Mobile friendly
Must be on a platform that i can update and make changes to it myself

```html
<!DOCTYPE html>
<html lang="en">
<head>
<meta charset="utf-8">
<title>Cellarlane – Contact Us</title>
<link rel="stylesheet" href="https://fonts.googleapis.com/css2?family=Oswald:wght@400;500&family=Roboto:wght@500;700&family=Lato:wght@400;700&family=IBM+Plex+Sans:wght@400;600&display=swap">
<style>
:root{
  --maroon:#7b0b1d;
  --red:#c4162a;
  --ink:#1c1c1c;
  --text:#333;
  --topbar:#231f20;
  --paper:#e9e9ea;
  --line:#cfcfcf;
  --footer:#161616;
  --white:#fff;
}
*{box-sizing:border-box;margin:0;padding:0}
html,body{width:1200px;height:2519px;overflow:hidden}
body{position:relative;background:var(--white);font-family:'Lato',sans-serif;color:var(--text)}
.abs{position:absolute}

/* top bar */
.topbar{left:0;top:0;width:1200px;height:33px;background:var(--topbar);color:var(--white);font:500 13px/33px 'Roboto',sans-serif;letter-spacing:.3px}
.topbar .item{position:absolute;top:0;display:flex;align-items:center;gap:6px}
.topbar svg{fill:var(--white)}
.social-dots{position:absolute;right:146px;top:11px;display:flex;gap:7px}
.social-dots span{width:10px;height:10px;border-radius:50%;background:var(--white)}

/* header */
.search{left:145px;top:63px;width:310px;height:44px;background:#f2f2f2;border:1px solid #e2e2e2;font-size:13px;color:#444;padding:0 18px;display:flex;align-items:center;justify-content:space-between}
.wholesale{left:831px;top:63px;width:152px;height:43px;border:2px solid var(--maroon);color:var(--maroon);font:500 15px/39px 'Oswald',sans-serif;text-align:center}
.cart{left:1015px;top:70px}
.cart-count{left:1038px;top:68px;width:13px;height:13px;border-radius:50%;background:#555;color:#fff;font-size:9px;line-height:13px;text-align:center}

.nav{left:0;top:137px;width:1200px;height:53px;background:var(--maroon)}
.nav a{position:absolute;top:0;color:var(--white);text-decoration:none;font:400 16px/53px 'Oswald',sans-serif}
.nav a.current{text-decoration:underline;text-underline-offset:4px}

.brand-disc{left:511px;top:14px;width:200px;height:180px;border-radius:50%;background:var(--white);display:flex;align-items:center;justify-content:center;flex-direction:column}
.brand-name{font:500 34px/1 'Oswald',sans-serif;color:var(--ink)}
.brand-mark{width:12px;height:12px;border-radius:50%;background:var(--maroon);margin-bottom:10px}

.hero{left:0;top:190px;width:1200px;height:331px;background:linear-gradient(100deg,#5b6e3c 0%,#c8a47e 25%,#8a6d4f 45%,#a89078 60%,#6a7a44 80%,#c49a78 100%)}

/* contact */
.contact{left:0;top:521px;width:1200px;height:806px;background:linear-gradient(90deg,#e4e4e5,#f0f0f1 50%,#e6e6e7)}
.section-title{position:absolute;left:0;width:1200px;text-align:center;font:700 38px/1 'Roboto',sans-serif;color:var(--ink)}
.rule{position:absolute;left:567px;width:66px;height:3px;background:var(--maroon)}
.intro{left:200px;top:172px;width:800px;text-align:center;font-size:17.5px;line-height:24px;color:#2b2b2b}
.intro b{color:var(--maroon);font-weight:700}
.field{position:absolute;background:var(--white);border:1px solid var(--line);font-size:13px;color:#333;padding:12px 16px}
.submit{left:518px;top:655px;width:163px;height:44px;background:var(--maroon);color:var(--white);font:500 16px/44px 'Roboto',sans-serif;text-align:center}

/* newsletter */
.news{left:0;top:1328px;width:661px;height:362px;background:radial-gradient(ellipse at 70% 60%,#3a3048 0%,#3f4a2c 45%,#2c3520 100%)}
.news h2{position:absolute;left:0;top:86px;width:726px;text-align:center;font:500 46px/1 'Oswald',sans-serif;color:var(--white);letter-spacing:-.5px}
.news p{position:absolute;left:0;top:149px;width:726px;text-align:center;color:var(--white);font-size:16px;line-height:25px}
.news-input{left:145px;top:216px;width:437px;height:39px;border-radius:20px;background:var(--white);font-size:12px;color:#444;padding:0 14px;line-height:39px}
.news-btn{left:445px;top:216px;width:137px;height:39px;border-radius:20px;background:var(--maroon);color:var(--white);font:500 14px/39px 'Roboto',sans-serif;text-align:center}
.brand-panel{left:661px;top:1328px;width:539px;height:362px;background:linear-gradient(90deg,#dcdcdc,#efefef 50%,#e2e2e2);display:flex;align-items:center;justify-content:center}
.brand-panel span{font:500 110px/1 'Oswald',sans-serif;color:var(--ink)}

/* partners */
.partner{position:absolute;top:1880px;width:140px;height:82px;border:1px solid #d6d6d6;background:var(--white);display:flex;align-items:center;justify-content:center}
.partner i{display:block;width:70px;height:22px;background:#e6e1da;border-radius:3px}
.arrow{position:absolute;top:1908px}

/* footer */
.footer{left:0;top:2058px;width:1200px;height:461px;background:radial-gradient(ellipse at 50% 30%,#242424,var(--footer))}
.foot-brand{left:160px;top:120px;font:500 46px/1 'Oswald',sans-serif;color:var(--white);display:flex;align-items:center;gap:10px}
.foot-brand em{width:14px;height:14px;border-radius:50%;border:2px solid var(--white)}
.foot-social{left:174px;top:2059px;display:flex;gap:4px}
.foot-social span{width:36px;height:36px;border:1.5px solid var(--white);border-radius:50%}
.col h3{font:600 18px/1 'IBM Plex Sans',sans-serif;color:var(--white);letter-spacing:.4px;margin-bottom:16px}
.col a{display:block;color:#e8e8e8;font:400 14px/26.4px 'IBM Plex Sans',sans-serif;text-decoration:none}
.contact-row{display:flex;align-items:center;gap:14px;color:#eee;font:400 16px/32px 'IBM Plex Sans',sans-serif}
.contact-row svg{width:18px}
.foot-rule{left:137px;top:2402px;width:936px;height:1px;background:#3a3a3a}
.copyright{left:0;top:2448px;width:1200px;text-align:center;color:#e8e8e8;font-size:16px}
</style>
</head>
<body>

<div class="abs topbar">
  <div class="item" style="left:145px">
    <svg width="12" height="12" viewBox="0 0 24 24"><path d="M6.6 10.8a15 15 0 0 0 6.6 6.6l2.2-2.2c.3-.3.7-.4 1-.2 1.1.4 2.3.6 3.6.6.6 0 1 .4 1 1V20c0 .6-.4 1-1 1A17 17 0 0 1 3 4c0-.6.4-1 1-1h3.5c.6 0 1 .4 1 1 0 1.3.2 2.5.6 3.6.1.3 0 .7-.2 1z"/></svg>
    TOLL FREE : 1300 555 019
  </div>
  <div class="item" style="left:368px">
    <svg width="13" height="13" viewBox="0 0 24 24"><path d="M12 2a10 10 0 1 0 0 20 10 10 0 0 0 0-20zm0 3a7 7 0 1 1 0 14 7 7 0 0 1 0-14zm-1 2v6l5 3 1-1.6-4-2.4V7z"/></svg>
    8AM-5PM MON-FRI
  </div>
  <div class="item" style="left:737px">
    <svg width="11" height="11" viewBox="0 0 24 24"><circle cx="12" cy="7" r="5"/><path d="M2 22c0-6 4-9 10-9s10 3 10 9z"/></svg>
    CORPORATE ACCOUNTS &nbsp;&nbsp;|&nbsp;&nbsp;
    <svg width="10" height="11" viewBox="0 0 20 24"><path d="M4 10V7a6 6 0 0 1 12 0v3h-3V7a3 3 0 0 0-6 0v3z"/><rect x="2" y="10" width="16" height="13" rx="1"/></svg>
    LOGIN
  </div>
  <div class="social-dots"><span></span><span></span><span></span></div>
</div>

<div class="abs search">Search products...
  <svg width="13" height="13" viewBox="0 0 24 24" fill="none" stroke="#333" stroke-width="3"><circle cx="10" cy="10" r="7"/><path d="M15 15l7 7"/></svg>
</div>
<div class="abs wholesale">WHOLESALE</div>
<svg class="abs cart" width="34" height="32" viewBox="0 0 34 32" fill="none" stroke="var(--maroon)" stroke-width="2.2" stroke-linejoin="round"><path d="M1 3h5l4 18h18l4-13H8"/><circle cx="12" cy="27" r="2.5"/><circle cx="26" cy="27" r="2.5"/></svg>
<div class="abs cart-count">0</div>

<nav class="abs nav">
  <a class="current" style="left:175px">HOME</a>
  <a style="left:240px">WINES</a>
  <a style="left:308px">BEER</a>
  <a style="left:367px">SPIRITS</a>
  <a style="left:443px">SPECIALS</a>
  <a style="left:722px">GIFT PACKS</a>
  <a style="left:817px">ABOUT US</a>
  <a style="left:905px">WINE CLUB</a>
  <a style="left:997px">CONTACT</a>
</nav>

<div class="abs brand-disc"><div class="brand-mark"></div><div class="brand-name">Cellarlane</div></div>

<div class="abs hero" role="img" aria-label="Group of friends laughing and sharing red wine in a vineyard"></div>

<section class="abs contact">
  <h1 class="section-title" style="top:92px">CONTACT US</h1>
  <div class="rule" style="top:145px"></div>
  <p class="abs intro">Our customer service department is here to help you from selecting wines, to account enquiries, delivery information and product descriptions. You can contact us <b>Monday - Friday 9am - 5pm AEST</b> except public holidays on <b>Tel:&nbsp; 1300 555 019 / Fax:&nbsp; 02 5550 0147</b> alternatively, you can complete the following form and we will respond as soon as possible.</p>
  <div class="field" style="left:249px;top:302px;width:344px;height:41px">First name</div>
  <div class="field" style="left:605px;top:302px;width:347px;height:41px">Email</div>
  <div class="field" style="left:249px;top:354px;width:344px;height:41px">Last Name</div>
  <div class="field" style="left:605px;top:354px;width:347px;height:41px">Phone</div>
  <div class="field" style="left:249px;top:413px;width:703px;height:208px">Message</div>
  <div class="abs submit">SUBMIT</div>
</section>

<section class="abs news" role="img" aria-label="Vineyard rows with bunches of dark grapes">
  <h2>JOIN OUR NEWSLETTER</h2>
  <p>Subscribe to our mailing list to receive updates<br>and promotional offers.</p>
  <div class="abs news-input">Enter your E - mail</div>
  <div class="abs news-btn">SUBSCRIBE</div>
</section>
<div class="abs brand-panel" role="img" aria-label="Brand name on light wood texture"><span>Cellarlane</span></div>

<h2 class="section-title" style="top:1768px">OUR PARTNERS</h2>
<div class="rule" style="top:1829px;left:560px;width:80px;background:var(--red)"></div>
<svg class="arrow" style="left:111px" width="12" height="22" viewBox="0 0 12 22" fill="none" stroke="#333" stroke-width="2.5"><path d="M10 2L2 11l8 9"/></svg>
<div class="partner" style="left:143px"><i></i></div>
<div class="partner" style="left:298px"><i></i></div>
<div class="partner" style="left:453px"><i></i></div>
<div class="partner" style="left:607px"><i></i></div>
<div class="partner" style="left:762px"><i></i></div>
<div class="partner" style="left:917px"><i></i></div>
<svg class="arrow" style="left:1075px" width="12" height="22" viewBox="0 0 12 22" fill="none" stroke="#333" stroke-width="2.5"><path d="M2 2l8 9-8 9"/></svg>

<footer class="abs footer">
  <div class="abs foot-brand"><em></em>Cellarlane</div>
  <div class="abs col" style="left:422px;top:82px">
    <h3>QUICK LINKS</h3>
    <a>Home</a><a>Wines</a><a>Beer</a><a>Spirits</a><a>Specials</a><a>About Us</a><a>Wine Club</a>
  </div>
  <div class="abs col" style="left:615px;top:82px">
    <h3>INFORMATION</h3>
    <a>Wholesale</a><a>Gift Packs</a><a>Corporate Accounts</a><a>Contact Us</a><a>International Shipping Info</a><a>Privacy &amp; Security</a><a>Satisfaction Guarantee</a>
  </div>
  <div class="abs col" style="left:846px;top:82px">
    <h3>CONACT US</h3>
    <div class="contact-row"><svg viewBox="0 0 24 24" fill="var(--red)"><path d="M6.6 10.8a15 15 0 0 0 6.6 6.6l2.2-2.2c.3-.3.7-.4 1-.2 1.1.4 2.3.6 3.6.6.6 0 1 .4 1 1V20c0 .6-.4 1-1 1A17 17 0 0 1 3 4c0-.6.4-1 1-1h3.5c.6 0 1 .4 1 1 0 1.3.2 2.5.6 3.6.1.3 0 .7-.2 1z"/></svg>1300 555 019</div>
    <div class="contact-row"><svg viewBox="0 0 24 18" fill="var(--red)"><path d="M0 0h24v2L12 10 0 2z"/><path d="M0 5l12 8 12-8v13H0z"/></svg>hello@cellarlane.com</div>
    <div class="contact-row" style="padding-left:32px;font-size:14px">8am-5pm Mon-Fri CST</div>
  </div>
</footer>
<div class="abs foot-social" style="top:2301px"><span></span><span></span><span></span></div>
<div class="abs foot-rule"></div>
<div class="abs copyright">© 2020 Cellarlane | All Rights Reserved | Disclaimer</div>

</body>
</html>
```